Business Card Design Project

Use newly designed logo and tie into newly designed website
I need a new logo and website layout designed for my partner's business. This is a birthday present. His business is interior painting, wallpapering and design. He also has access to a wide variety of products including carpet, fabrics, furniture, wallpaper, tile, countertops, etc. I have attached some screen shots of his website for reference. He is a one man shop and has a stellar reputation with his customers. He is on-time, very tidy, excellent with animals, and always finishes on time and on budget. There are no restrictions on colors or fonts. The logo needs to work well with the website, business cards and printed materials. The website needs to flow content for device size so it looks just as good on a cell phone or tablet as it does on a desktop computer. Whatever the heck that's called!Thanks. I am looking forward to seeing everyone's ideas.
Updates
Hi Designers,
We've reopened this project as our logo design project has just completed.
Please refer to the uploaded files and make use of either Horizontal or Vertical versions of the logo depending on what you think is suitable for your design proposals.
We look forward to your creative submissions!
Target Market(s)
Consumers looking to improve the interior environment of their homes by updating wall paint or paper, flooring (either carpet, tile, or hardwoods), counter tops, window treatments, etc. Clients tend to be more upper middle class and have certain taste levels and expectations. New logo, website and business card should align to meet those levels.
Industry/Entity Type
Cell Phone
Look and feel
Each slider illustrates characteristics of the customer's brand and the style your logo design should communicate.

```html
<!DOCTYPE html>
<html lang="en">
<head>
<meta charset="utf-8">
<title>Vellano Interior Designs – Business Card</title>
<link rel="stylesheet" href="https://fonts.googleapis.com/css2?family=Cinzel:wght@500;700&family=Dosis:wght@400;500&display=swap">
<style>
  :root {
    --stage: #2b2b2e;
    --card-white: #ffffff;
    --plum: #2d2446;
    --gold: #a88f5c;
    --wine: #8c1c22;
    --ink: #2d2446;
    --contact: #f2eff7;
  }
  * { box-sizing: border-box; margin: 0; padding: 0; }
  html, body {
    width: 1200px; height: 780px; overflow: hidden;
    background: var(--stage);
  }
  .canvas {
    position: relative; width: 1200px; height: 780px;
  }
  .card {
    position: absolute; left: 110px; top: 110px;
    width: 980px; height: 560px;
    background: var(--card-white);
    overflow: hidden;
    box-shadow: 0 14px 40px rgba(0,0,0,.45);
  }
  .card-shapes { position: absolute; inset: 0; }
  .holder-name {
    position: absolute; left: 62px; top: 118px;
    font-family: "Cinzel", serif; font-weight: 700;
    font-size: 40px; color: var(--wine); letter-spacing: 1px;
  }
  .contact-list {
    position: absolute; left: 58px; top: 352px;
    list-style: none;
    font-family: "Dosis", sans-serif; font-weight: 400;
    font-size: 24px; color: var(--contact);
  }
  .contact-list li {
    display: flex; align-items: center; gap: 16px;
    height: 36px;
  }
  .contact-list svg { width: 20px; height: 20px; flex: none; }
  .brand {
    position: absolute; left: 600px; top: 190px; width: 330px;
    display: flex; flex-direction: column; align-items: center;
    font-family: "Cinzel", serif; font-weight: 700; color: var(--ink);
    text-align: center;
  }
  .brand-mark {
    width: 150px; height: 150px; background: var(--ink); margin-bottom: 18px;
  }
  .brand-name { font-size: 50px; letter-spacing: 3px; line-height: 1; }
  .brand-tagline { font-size: 24px; letter-spacing: 2px; margin-top: 6px; }
</style>
</head>
<body>
<main class="canvas">
  <section class="card" aria-label="Business card for Vellano Interior Designs">
    <svg class="card-shapes" viewBox="0 0 980 560" aria-hidden="true">
      <rect width="980" height="560" fill="var(--plum)"/>
      <circle class="ring-right" cx="790" cy="250" r="370" fill="var(--gold)"/>
      <circle class="disc-right" cx="790" cy="250" r="352" fill="var(--card-white)"/>
      <circle class="ring-left" cx="245" cy="-60" r="322" fill="var(--gold)"/>
      <circle class="disc-left" cx="245" cy="-60" r="304" fill="var(--card-white)"/>
    </svg>

    <h1 class="holder-name">Dario Vellano</h1>

    <ul class="contact-list">
      <li>
        <svg viewBox="0 0 20 20"><rect x="6" y="2" width="8" height="16" rx="1.5" fill="none" stroke="currentColor" stroke-width="1.8"/><circle cx="10" cy="15" r="1" fill="currentColor"/></svg>
        (555) 214-3098
      </li>
      <li>
        <svg viewBox="0 0 20 20"><rect x="2" y="5" width="16" height="11" fill="none" stroke="currentColor" stroke-width="1.6"/><path d="M2 5l8 6 8-6" fill="none" stroke="currentColor" stroke-width="1.6"/></svg>
        dario@vellanodesigns.com
      </li>
      <li>
        <svg viewBox="0 0 20 20"><circle cx="10" cy="10" r="7.5" fill="none" stroke="currentColor" stroke-width="1.6"/><ellipse cx="10" cy="10" rx="3.2" ry="7.5" fill="none" stroke="currentColor" stroke-width="1.4"/><path d="M2.5 10h15" stroke="currentColor" stroke-width="1.4"/></svg>
        www.vellanodesigns.com
      </li>
      <li>
        <svg viewBox="0 0 20 20"><path d="M10 19s-6-6.5-6-11a6 6 0 0 1 12 0c0 4.5-6 11-6 11z" fill="currentColor"/><circle cx="10" cy="8" r="2.2" fill="var(--plum)"/></svg>
        4820 W Linden Ct. Fairview, KS 66000
      </li>
    </ul>

    <div class="brand">
      <span class="brand-mark"></span>
      <span class="brand-name">VELLANO</span>
      <span class="brand-tagline">INTERIOR DESIGNS</span>
    </div>
  </section>
</main>
</body>
</html>
```